Velmar Intergrated Marketing Stationary Design Contest

We require a very professional looking stationary set to include: letterhead, compliments slip and business cards (double sided bus cards).

Files should be supplied on either Illustrator or InDesign.

We are interested in perhaps encorporating a faint watermark with the letter q or the logo, but it isnt a pre-requisite

Target Market(s)

Business owners seeking professional marketing services

Industry/Entity Type

Marketing

Requirements
Must have
• Concurrent theme wiht business cards, letterhead and comp slip. Must be an editable document for future ammendment
Should not have
• No use of times new roman or similar fonts

```html
<!DOCTYPE html>
<html lang="en">
<head>
<meta charset="utf-8">
<title>Velmar Stationery Set</title>
<link rel="stylesheet" href="https://fonts.googleapis.com/css2?family=Carlito:wght@400;700&family=Pinyon+Script&display=swap">
<style>
  :root {
    --bg: #ff807c;
    --edge: #e2696e;
    --teal: #0f7a78;
    --purple: #7b4fd0;
  }
  html, body { margin: 0; padding: 0; overflow: hidden; }
  body { width: 1200px; height: 842px; background: var(--bg); font-family: "Carlito", "Calibri", sans-serif; color: var(--teal); }
  .canvas { position: relative; width: 1200px; height: 842px; overflow: hidden; }
  .sheet { position: absolute; border: 1px solid var(--edge); box-sizing: border-box; }

  .brand-name { position: absolute; margin: 0; color: var(--teal); font-weight: 400; line-height: 1; white-space: nowrap; }

  .address { position: absolute; text-align: right; font-size: 9px; line-height: 12.1px; margin: 0; }
  .contacts { position: absolute; list-style: none; margin: 0; padding: 0; font-size: 9px; line-height: 12.1px; text-align: right; }
  .contacts .key { color: var(--purple); display: inline-block; width: 10px; text-align: right; }

  /* business card back */
  .card-back { left: 333px; top: 134px; width: 251px; height: 140px; }
  .card-back .brand-name { right: 16px; top: 88px; font-size: 30px; }

  /* business card front */
  .card-front { left: 333px; top: 289px; width: 251px; height: 140px; }
  .card-front .brand-name { left: 10px; top: 9px; font-size: 20px; }
  .person { position: absolute; right: 8px; top: 16px; text-align: right; }
  .person-name { color: var(--purple); font-size: 12px; line-height: 12px; }
  .person-role { font-size: 6px; line-height: 7px; text-transform: uppercase; }
  .card-front .address { right: 8px; top: 57px; }
  .card-front .contacts { left: 10px; top: 81px; text-align: left; }
  .card-front .contacts .key { width: 16px; text-align: left; }

  /* compliments slip */
  .comp-slip { left: 52px; top: 474px; width: 535px; height: 241px; }
  .comp-slip .brand-name { left: 24px; top: 20px; font-size: 38px; }
  .comp-slip .address { right: 23px; top: 16px; }
  .comp-slip .contacts { right: 26px; top: 91px; }
  .compliments { position: absolute; right: 28px; top: 158px; margin: 0; font-family: "Pinyon Script", cursive; font-weight: 400; font-size: 48px; color: var(--purple); line-height: 1; white-space: nowrap; }

  /* letterhead */
  .letterhead { left: 608px; top: 47px; width: 535px; height: 755px; }
  .letterhead .brand-name { right: 35px; top: 28px; font-size: 40px; }
  .letterhead .address { right: 35px; top: 87px; }
  .letterhead .contacts { right: 38px; top: 162px; }
  .legal { position: absolute; left: 79px; top: 716px; display: flex; gap: 18px; font-size: 9px; margin: 0; padding: 0; list-style: none; white-space: nowrap; }
</style>
</head>
<body>
<main class="canvas">

  <section class="sheet card-back" aria-label="Business card, back">
    <p class="brand-name">Velmar</p>
  </section>

  <section class="sheet card-front" aria-label="Business card, front">
    <p class="brand-name">Velmar</p>
    <div class="person">
      <div class="person-name">Dana Hollis</div>
      <div class="person-role">General Manager</div>
    </div>
    <p class="address">Velmar Intergrated Marketing<br>Harbour House<br>Mill Lane<br>Ashbridge<br>North Fenshire<br>AB12 3CD</p>
    <ul class="contacts">
      <li><span class="key">W</span>www.velmarim.co.uk</li>
      <li><span class="key">E</span>dana@velmarim.co.uk</li>
      <li><span class="key">T</span>01632 960214</li>
      <li><span class="key">F</span>01632 960211</li>
    </ul>
  </section>

  <section class="sheet comp-slip" aria-label="Compliments slip">
    <p class="brand-name">Velmar</p>
    <p class="address">Velmar Intergrated Marketing<br>Harbour House<br>Mill Lane<br>Ashbridge<br>North Fenshire<br>AB12 3CD</p>
    <ul class="contacts">
      <li>www.velmarim.co.uk <span class="key">W</span></li>
      <li>enquiries@velmarim.co.uk <span class="key">E</span></li>
      <li>01632 960214 <span class="key">T</span></li>
      <li>01632 960211 <span class="key">F</span></li>
    </ul>
    <p class="compliments">With Compliments</p>
  </section>

  <section class="sheet letterhead" aria-label="Letterhead">
    <p class="brand-name">Velmar</p>
    <p class="address">Velmar Intergrated Marketing<br>Harbour House<br>Mill Lane<br>Ashbridge<br>North Fenshire<br>AB12 3CD</p>
    <ul class="contacts">
      <li>www.velmarim.co.uk <span class="key">W</span></li>
      <li>enquiries@velmarim.co.uk <span class="key">E</span></li>
      <li>01632 960214 <span class="key">T</span></li>
      <li>01632 960211 <span class="key">F</span></li>
    </ul>
    <ul class="legal">
      <li>Company registration&nbsp; 4815162</li>
      <li>Vat No. 918 2736 45</li>
      <li>Trading as a division of Brenford Ltd</li>
    </ul>
  </section>

</main>
</body>
</html>
```